BrivaTrek Freight Services Business cards

Would like a very unique design catchy but professional for business cards. Please use log provided.Marlon WellsCeo and Founder TransCon Logistix Solutions1-888-913-3225mwells@tlsolutionsus.comwww.bfservicesco.com

```html
<!DOCTYPE html>
<html lang="en">
<head>
<meta charset="utf-8">
<title>BrivaTrek Freight Services – Business Cards</title>
<link rel="stylesheet" href="https://fonts.googleapis.com/css2?family=Lato:wght@400;700;900&family=Cinzel:wght@600&display=swap">
<style>
  :root {
    --backdrop: #3a302b;
    --card: #121212;
    --card-edge: #1d1d1d;
    --brand-blue: #1a73c4;
    --brand-red: #e8262d;
    --text-light: #d6d6d6;
    --divider: #3a3a3a;
    --silver: #c9c9c9;
  }
  * { margin: 0; padding: 0; box-sizing: border-box; }
  html, body { width: 1200px; height: 844px; overflow: hidden; }
  body {
    background: var(--backdrop);
    font-family: "Lato", sans-serif;
    position: relative;
  }
  .card {
    position: absolute;
    width: 520px;
    height: 297px;
    background: var(--card);
    border: 1px solid var(--card-edge);
    box-shadow: 0 14px 30px rgba(0,0,0,0.45);
  }
  .card-front { left: 50px; top: 274px; }
  .card-back { left: 630px; top: 274px; }

  /* front */
  .front-brand {
    position: absolute;
    left: 30px;
    top: 0;
    bottom: 0;
    width: 190px;
    display: flex;
    align-items: center;
    gap: 10px;
  }
  .front-brand .brand-square {
    width: 18px; height: 18px;
    background: var(--brand-red);
    flex: none;
  }
  .front-brand .brand-name {
    font-family: "Lato", sans-serif;
    font-weight: 900;
    font-size: 22px;
    line-height: 1.1;
    color: var(--brand-blue);
    text-transform: uppercase;
  }
  .front-divider {
    position: absolute;
    left: 240px;
    top: 40px;
    bottom: 40px;
    width: 1px;
    background: var(--divider);
  }
  .contact {
    position: absolute;
    left: 262px;
    top: 78px;
    color: var(--text-light);
  }
  .contact .person-name {
    font-weight: 900;
    font-size: 20px;
    letter-spacing: 0.5px;
    text-transform: uppercase;
  }
  .person-name .first { color: var(--brand-blue); }
  .person-name .last { color: var(--brand-red); }
  .contact .person-role {
    font-size: 14px;
    margin: 2px 0 14px;
  }
  .contact-list { list-style: none; }
  .contact-list li {
    display: flex;
    align-items: center;
    gap: 8px;
    font-size: 14px;
    line-height: 22px;
  }
  .contact-list svg { width: 12px; height: 12px; fill: var(--brand-blue); flex: none; }

  /* back */
  .back-brand {
    position: absolute;
    inset: 0;
    display: flex;
    flex-direction: column;
    align-items: center;
    justify-content: center;
    gap: 14px;
  }
  .back-brand .brand-name {
    font-family: "Cinzel", serif;
    font-weight: 600;
    font-size: 30px;
    color: var(--silver);
    text-align: center;
    line-height: 1.2;
  }
  .back-brand .brand-rule {
    width: 260px;
    height: 1px;
    background: var(--silver);
  }
</style>
</head>
<body>
  <section class="card card-front">
    <div class="front-brand">
      <span class="brand-square"></span>
      <span class="brand-name">BrivaTrek Freight Services</span>
    </div>
    <div class="front-divider"></div>
    <div class="contact">
      <p class="person-name"><span class="first">Dustin</span> <span class="last">Harrow</span></p>
      <p class="person-role">CEO and Founder</p>
      <ul class="contact-list">
        <li>
          <svg viewBox="0 0 24 24" aria-hidden="true"><path d="M6.6 10.8a15.1 15.1 0 0 0 6.6 6.6l2.2-2.2a1 1 0 0 1 1-.25 11.4 11.4 0 0 0 3.6.57 1 1 0 0 1 1 1V20a1 1 0 0 1-1 1A17 17 0 0 1 3 4a1 1 0 0 1 1-1h3.5a1 1 0 0 1 1 1c0 1.25.2 2.45.57 3.6a1 1 0 0 1-.25 1z"/></svg>
          1-888-472-6081
        </li>
        <li>
          <svg viewBox="0 0 24 24" aria-hidden="true"><path d="M2 5h20v14H2z M2 5l10 8 10-8" fill="none" stroke="#1a73c4" stroke-width="2.5"/></svg>
          dharrow@bfservicesco.com
        </li>
        <li>
          <svg viewBox="0 0 24 24" aria-hidden="true"><circle cx="12" cy="12" r="10"/></svg>
          www.bfservicesco.com
        </li>
      </ul>
    </div>
  </section>

  <section class="card card-back">
    <div class="back-brand">
      <span class="brand-name">BrivaTrek Freight Services</span>
      <span class="brand-rule"></span>
    </div>
  </section>
</body>
</html>
```